Spannish marketing agency needs redesign of powerpoint presentation for client acquisition

We want to redesign our powerpoint presentation. We use this presentation to show our clients how we work. WE NEED IT TO BE IN POWERPOINT FORMAT
The style should match the style of our logo and story brand, but apart from that we want designers to get creative.
Updates
The project must be in powerpoint format. The project must be in powerpoint format
Baja calidad de diseño
Target Market(s)
Small and medium size business owners
Industry/Entity Type
Digital marketing
Look and feel
Each slider illustrates characteristics of the customer's brand and the style your logo design should communicate.

```html
<!DOCTYPE html>
<html lang="es">
<head>
<meta charset="UTF-8">
<title>Nuestro proceso</title>
<link rel="stylesheet" href="https://fonts.googleapis.com/css2?family=Montserrat:wght@600;700;800&display=swap">
<style>
  :root {
    --brand-blue: #0066cc;
    --ink-navy: #0d1633;
    --paper: #ffffff;
  }
  * { margin: 0; padding: 0; box-sizing: border-box; }
  html, body { width: 1200px; height: 675px; overflow: hidden; background: var(--paper); }
  .slide {
    position: relative;
    width: 1200px;
    height: 675px;
    background: var(--paper);
    font-family: "Montserrat", sans-serif;
    color: var(--ink-navy);
    overflow: hidden;
  }
  .brand-name {
    position: absolute;
    top: 52px;
    right: 38px;
    font-size: 24px;
    font-weight: 600;
    letter-spacing: 0.14em;
    color: var(--ink-navy);
  }
  .process-line {
    position: absolute;
    left: 131px;
    width: 938px;
    top: 408px;
    height: 3px;
    background: var(--brand-blue);
  }
  .step {
    position: absolute;
    top: 0;
    width: 240px;
    height: 675px;
    margin-left: -120px;
  }
  .step > * { position: absolute; left: 50%; transform: translateX(-50%); }
  .step-icon { top: 233px; width: 64px; height: 64px; }
  .step-number {
    top: 322px;
    height: 50px;
    font-size: 48px;
    font-weight: 800;
    line-height: 50px;
  }
  .step-marker {
    top: 393px;
    width: 34px;
    height: 34px;
    border-radius: 50%;
    background: var(--paper);
    border: 2px solid var(--brand-blue);
    display: flex;
    align-items: center;
    justify-content: center;
  }
  .step-marker::after {
    content: "";
    width: 19px;
    height: 19px;
    border-radius: 50%;
    background: var(--brand-blue);
  }
  .step-label {
    top: 451px;
    width: 240px;
    font-size: 14px;
    font-weight: 700;
    line-height: 18px;
    letter-spacing: 0.12em;
    text-align: center;
    text-transform: uppercase;
  }
  .footer-band {
    position: absolute;
    left: 0;
    bottom: 0;
    width: 1200px;
    height: 31px;
    background: var(--brand-blue);
  }
  .icon-line { fill: none; stroke: var(--brand-blue); stroke-width: 6; stroke-linecap: butt; stroke-linejoin: round; }
  .icon-fill { fill: var(--brand-blue); }
</style>
</head>
<body>
<main class="slide">
  <div class="brand-name">FLAMORA</div>

  <div class="process-line"></div>

  <section class="step" style="left:131px">
    <svg class="step-icon" viewBox="0 0 64 64" aria-hidden="true">
      <circle class="icon-line" cx="24" cy="24" r="16"/>
      <line class="icon-line" x1="36" y1="36" x2="55" y2="55" stroke-width="7"/>
    </svg>
    <div class="step-number">1</div>
    <div class="step-marker"></div>
    <p class="step-label">Análisis inicial</p>
  </section>

  <section class="step" style="left:366px">
    <svg class="step-icon" viewBox="0 0 64 64" aria-hidden="true">
      <path class="icon-line" d="M60 3 C44 3 32 12 22 28 L36 42 C52 32 61 20 60 3 Z"/>
      <circle class="icon-fill" cx="42" cy="22" r="5"/>
      <path class="icon-line" d="M22 28 L10 26 L4 35 L16 33"/>
      <path class="icon-line" d="M36 42 L38 54 L29 60 L31 48"/>
      <path class="icon-fill" d="M13 42 C6 45 4 54 3 62 C11 61 20 59 22 51 Z"/>
    </svg>
    <div class="step-number">2</div>
    <div class="step-marker"></div>
    <p class="step-label">Identidad de<br>marca</p>
  </section>

  <section class="step" style="left:600px">
    <svg class="step-icon" viewBox="0 0 64 64" aria-hidden="true">
      <rect class="icon-line" x="3" y="5" width="58" height="52" rx="3"/>
      <rect class="icon-fill" x="12" y="15" width="14" height="5"/>
      <rect class="icon-fill" x="12" y="28" width="14" height="5"/>
      <rect class="icon-fill" x="12" y="41" width="14" height="5"/>
      <path class="icon-line" d="M32 30 L39 37 L52 22"/>
    </svg>
    <div class="step-number">3</div>
    <div class="step-marker"></div>
    <p class="step-label">Objetivos de<br>nuestra empresa</p>
  </section>

  <section class="step" style="left:834px">
    <svg class="step-icon" viewBox="0 0 64 64" aria-hidden="true">
      <path class="icon-line" d="M5 5 L30 5 L60 35 L35 60 L5 30 Z"/>
      <circle class="icon-fill" cx="15" cy="15" r="4.5"/>
      <path class="icon-fill" d="M34 50 L22 38 C18 34 20 28 25 28 C28 28 30 30 33 33 C36 30 38 28 41 28 C46 28 48 34 44 38 Z"/>
    </svg>
    <div class="step-number">4</div>
    <div class="step-marker"></div>
    <p class="step-label">Recorrido del<br>comprador</p>
  </section>

  <section class="step" style="left:1069px">
    <svg class="step-icon" viewBox="0 0 64 64" aria-hidden="true">
      <circle class="icon-line" cx="25" cy="14" r="9"/>
      <path class="icon-line" d="M28 34 C16 34 6 38 6 46 L6 50 L30 50"/>
      <circle class="icon-line" cx="42" cy="40" r="10"/>
      <line class="icon-line" x1="49" y1="47" x2="60" y2="58" stroke-width="7"/>
    </svg>
    <div class="step-number">5</div>
    <div class="step-marker"></div>
    <p class="step-label">Definición de<br>equipo<br>profesional</p>
  </section>

  <div class="footer-band"></div>
</main>
</body>
</html>
```